依頼詳細
企画内容や入れた欲しい文言は添付資料にあります。(A4で2枚分)
文字の大きさや赤字は私が強調したいと考えているイメージと捉えてください。
また、文言・キャッチ等の変更の提案は大歓迎です。是非勉強させてください!

イメージしている事
・女性がターゲットになっているような雰囲気。
・当たり障りのないというよりは、どこか振り切れているような個性的な雰囲気。
・「頑張ってやってくれそうね。」という印象を持ってもらいたい。
今回ワークテラスさんに依頼するのは、2回目ですが前回(下敷きのデザイン)は、ワークテラスさんの色々な提案により当初イメージしていたものよりいい物ができたので、色々な提案や質問は大歓迎です。

また、出来れば今回の依頼の中で、今後も定期的にデザインをお願いできる方がいればという事を兼ねているので、定期的に(大体「月1」位のペース)お願いできる方はその旨お伝えください。

私が選考するポイント
・キャッチやレイアウト等、ターゲットからのレスポンスがありそうか?
私はチラシは如何にして見て読んだ瞬間にアクション(問い合わせ)を起こさせるかがポイントだと思っています。
・レスポンスの速さ(私は速くないですが)等の対応
記載項目
屋号:学習塾 ミナリオ
電話番号:047-513-8847
URL:http://minario-juku.jp/
※ 二次元コードとロゴは添付資料よりおとりください。
サイズ
B4
ページ数
両面
希望イメージ
シンプル 複雑
単色 カラフル
暗い 明るい
日常 高級
遊び心 厳粛
未来的 伝統的
女性的 男性的
希望する色
大きな希望はないですが、塾のイメージはオレンジです。
納品ファイル
• 高解像度JPG (.jpg)
• イラストレーター形式 (.ai)
• フォトショップ形式 (.psd)
補足説明
今回のチラシでは、塾長をある程度前面に出した形にしようと思っているので、
「ここにこんなポーズの写真をいれましょう!」
などのご提案も受け付けます。
言っていただければ、はめ込みもしやすいように白バックで撮ってお渡しします。

また、チラシの依頼は初めてなので説明の足りない箇所等あると思いますので、
その際はお手数ですが、ご質問ください。
キャンペーン面の下部に
「HPに『無料体験者の感想』を掲載しています」
とHPに誘導する仕組みを作成してください。
塾長の写真をアップしました。
ご確認ください。
たくさんのご提案ありがとうございました。
依頼の段階でもお伝えした通り、できれば今後も定期的にお願いできる方が希望です。
定期的な依頼が可能なのに、その旨お伝えいただいていない方はメッセージ等で、その旨ご連絡ください。

選定段階(修正依頼等)に入りましたら、またこの欄にてご報告させていただきます。
(少なくとも金曜日までにはアクションをおこします。)

本当にたくさんのご提案ありがとうございました。
■ 選んだ理由

私の当初のイメージ(熱意がありそう・ちゃんとした塾でありそう)
に、一番近かった事が最大の決め手でした。
また、私が添付したデータはただ腕組みをしている写真でしたが、
動きのある写真の方がいいなぁと、漠然には感じていた所も大きいかと思います。

■ 提案者全員のお礼・コメント

この度は、弊社の依頼にご提案いただき誠にありがとうございました。
正直、選考するのにかなり悩みました。
私が、原案の中で気になっていた箇所をうまくまとめていただいた方、
文言の言い回しの修正の仕方など、とても勉強になりました。
また、依頼をさせていただく際には、是非ご提案いただければと思います。

```html
<!DOCTYPE html>
<html lang="ja">
<head>
<meta charset="utf-8">
<title>学習塾 ミナリオ 中間特講</title>
<link rel="stylesheet" href="https://fonts.googleapis.com/css2?family=Noto+Sans+JP:wght@400;700;900&family=Noto+Serif+JP:wght@700;900&display=swap">
<style>
:root{
  --orange:#f08a1c;
  --orange-deep:#e3701a;
  --red:#d9262b;
  --pink:#fbe3e0;
  --yellow:#fbd33b;
  --cream:#fff7d6;
  --green:#d9eaa6;
  --green-line:#a8c95a;
  --ink:#333;
  --white:#fff;
}
*{box-sizing:border-box;margin:0;padding:0}
html,body{width:872px;height:1200px;overflow:hidden;background:var(--white)}
body{font-family:"Noto Sans JP",sans-serif;color:var(--ink);position:relative}
.flyer{position:absolute;inset:0;border:10px solid var(--orange);overflow:hidden}

.hero{position:absolute;left:0;top:0;width:852px;height:640px}
.catch{position:absolute;left:24px;top:20px;writing-mode:vertical-rl;font-family:"Noto Serif JP",serif;font-weight:900;color:var(--orange);font-size:62px;letter-spacing:2px;line-height:1.15}
.catch .strong{color:var(--orange-deep);font-size:74px}
.portrait{position:absolute;left:180px;top:40px;width:400px;height:600px;background:linear-gradient(180deg,#f2f2f2 0%,#d8d8d8 55%,#5a5a5a 100%)}
.caption{position:absolute;left:24px;top:560px;width:140px;background:var(--white);border:1px solid var(--orange);padding:5px 8px;font-size:13px;line-height:1.4;color:var(--orange-deep);font-weight:700}

.badge{position:absolute;left:598px;top:14px;width:244px;height:244px;border-radius:50%;background:radial-gradient(circle,var(--white) 0%,var(--white) 62%,var(--pink) 100%)}
.badge-text{position:absolute;left:598px;top:40px;width:244px;text-align:center;color:var(--red);font-family:"Noto Serif JP",serif;font-weight:900}
.badge-text .small{font-size:22px;display:block}
.badge-text .big{font-size:54px;line-height:1.1;display:block}
.badge-text .big span{font-size:32px}
.badge-text .promise{font-size:58px;display:block;line-height:1.1}

.pitch{position:absolute;left:578px;top:400px;width:266px;height:140px;background:var(--yellow);padding:12px;text-align:center}
.pitch .lead{font-size:16px;font-weight:700}
.pitch .main{font-family:"Noto Serif JP",serif;font-size:32px;font-weight:900;line-height:1.25}
.pitch .sub{font-size:22px;font-weight:900;color:var(--red)}
.course-name{position:absolute;left:578px;top:548px;width:266px;text-align:center;font-family:"Noto Serif JP",serif;font-size:38px;font-weight:900;color:var(--orange-deep)}
.course-note{position:absolute;left:590px;top:602px;width:246px;text-align:center;font-size:10px;color:var(--orange-deep);line-height:1.4}

.course{position:absolute;left:0;top:640px;width:852px;height:430px;background:var(--green)}
.course-title{position:absolute;left:0;top:24px;width:852px;text-align:center;font-size:22px;font-weight:900}
.course-quote{position:absolute;left:100px;top:62px;width:652px;text-align:center;background:var(--cream);border:2px solid var(--green-line);font-family:"Noto Serif JP",serif;font-size:28px;font-weight:900;color:var(--red);padding:4px 0}
.details{position:absolute;left:28px;top:130px;width:480px;border-collapse:collapse;font-size:13px;line-height:1.6}
.details th{width:92px;text-align:left;color:var(--red);font-weight:700;vertical-align:top;padding:1px 0}
.details td{padding:1px 0}
.schedule{position:absolute;left:28px;top:300px;width:500px;background:var(--white);border:2px solid var(--green-line);border-collapse:collapse;font-size:13px;line-height:1.6}
.schedule th{width:90px;background:var(--green-line);color:var(--white);font-weight:700;padding:4px 8px;text-align:center;border-bottom:1px solid var(--white)}
.schedule td{padding:4px 10px;border-bottom:1px solid var(--green)}
.contact{position:absolute;left:540px;top:130px;width:290px;font-size:13px;line-height:1.6}
.contact .tel{color:var(--red);font-weight:900;font-size:16px}
.good{position:absolute;left:690px;top:290px;width:130px;height:120px;border-radius:50%;background:var(--yellow);display:flex;align-items:center;justify-content:center;font-size:28px;font-weight:900}

.footer{position:absolute;left:0;top:1070px;width:852px;height:110px;background:var(--white);border-top:3px solid var(--orange);display:flex;align-items:center;padding:0 20px;gap:20px}
.brand{display:flex;align-items:center;gap:8px;font-size:26px;font-weight:900;color:var(--orange)}
.brand i{width:22px;height:22px;background:var(--orange);display:block}
.phone{display:flex;align-items:center;gap:8px;font-size:30px;font-weight:900}
.phone small{font-size:11px;font-weight:400;display:block}
.web{margin-left:auto;text-align:right}
.search{display:flex;border:2px solid var(--orange);font-size:14px;font-weight:700}
.search b{background:var(--orange);color:var(--white);padding:4px 8px}
.search span{padding:4px 40px 4px 10px}
.search em{font-style:normal;background:var(--yellow);padding:4px 8px}
.url{font-size:13px;margin-top:4px}
</style>
</head>
<body>
<div class="flyer">
  <section class="hero">
    <h1 class="catch">今からでも<br><span class="strong">大丈夫!</span></h1>
    <div class="portrait" role="img" aria-label="スーツ姿で腕を広げる塾長の写真"></div>
    <p class="caption">学習塾 ミナリオ 塾長<br>数学担当</p>

    <div class="badge" role="img" aria-label="リボン付きの丸い保証バッジ"></div>
    <div class="badge-text">
      <span class="small">中間テスト</span>
      <span class="big">20<span>点</span>UP</span>
      <span class="promise">保証!!</span>
    </div>

    <div class="pitch">
      <p class="lead">定期テスト対策塾がみせる</p>
      <p class="main">本物の指導力</p>
      <p class="sub">塾長直伝!</p>
    </div>
    <p class="course-name">「中間特講」</p>
    <p class="course-note">上がらなかったら授業料全額返金して<br>補習授業を実施します</p>
  </section>

  <section class="course">
    <h2 class="course-title">塾長が直接指導!中間テスト短期特訓講座</h2>
    <p class="course-quote">「数学嫌いな若者よ!いつまでも逃げちゃダメだ!」</p>

    <table class="details">
      <tr><th>【対象学年】</th><td>中学1年生〜中学3年生(各学年定員あり)</td></tr>
      <tr><th>【実施期間】</th><td>中間テスト前の三週間・毎週土曜日に実施</td></tr>
      <tr><th>【受講料】</th><td>数学1科目 全6回 12,000円(教材費込み)</td></tr>
      <tr><th>【お申込み】</th><td>お電話または塾の窓口にて受付しています</td></tr>
      <tr><th>【20点UP】</th><td>前回の定期テストと比べて点数を判定します</td></tr>
      <tr><th>【注意事項】</th><td>全回出席と宿題の提出が保証の条件です</td></tr>
    </table>

    <table class="schedule">
      <tr><th>1年生</th><td>土曜 14:00〜16:00 正負の数・文字式を徹底演習</td></tr>
      <tr><th>2年生</th><td>土曜 16:30〜18:30 式の計算・連立方程式を特訓</td></tr>
      <tr><th>3年生</th><td>土曜 19:00〜21:00 展開・因数分解・平方根を攻略</td></tr>
    </table>

    <div class="contact">
      <p>お問い合わせ・お申込みは</p>
      <p class="tel">TEL 047-513-8847</p>
      <p>受付時間 平日15:00〜21:00</p>
      <p>ホームページからもお申込みいただけます。</p>
      <p>詳しくは 学習塾 ミナリオ で検索!</p>
    </div>

    <div class="good" role="img" aria-label="Good と書かれた花形の飾り">Good</div>
  </section>

  <footer class="footer">
    <div class="brand"><i></i>ミナリオ</div>
    <div class="phone">
      <svg width="30" height="30" viewBox="0 0 24 24" aria-hidden="true"><path fill="#333" d="M6.6 10.8a15 15 0 0 0 6.6 6.6l2.2-2.2c.3-.3.7-.4 1-.2 1.1.4 2.3.6 3.6.6.6 0 1 .4 1 1V20c0 .6-.4 1-1 1A17 17 0 0 1 3 4c0-.6.4-1 1-1h3.5c.6 0 1 .4 1 1 0 1.3.2 2.5.6 3.6.1.3 0 .7-.2 1z"/></svg>
      <div><small>その他ご不明な点もお気軽にお問い合わせください</small>047-513-8847</div>
    </div>
    <div class="web">
      <div class="search"><b>SEARCH</b><span>学習塾 ミナリオ</span><em>GO</em></div>
      <p class="url">http://minario-juku.jp/</p>
    </div>
  </footer>
</div>
</body>
</html>
```